Full re-design of visual identity

We have just re-designed our logo and would like to apply it on our folders, business cards, stationery, and etc... we are attaching new logo + the material we need to re-design... we will provide full corel draw files to help make job easier and also because lot of icons and artwork can be still used...

any doubts we are at your disposal. thanks in advance.

Business

```html
<!DOCTYPE html>
<html lang="pt">
<head>
<meta charset="utf-8">
<title>Lumora – Stationery Set</title>
<link href="https://fonts.googleapis.com/css2?family=Arimo:wght@400;700&display=swap" rel="stylesheet">
<style>
  :root{
    --bg:#7d7d7d;
    --paper:#ffffff;
    --paper-soft:#f1f1f1;
    --ink:#3a3a3a;
    --ink-soft:#6b6b6b;
    --brand-grey:#5c5c5c;
    --orange:#ee6a10;
    --orange-deep:#c9500a;
    --rule:#b9b9b9;
  }
  *{box-sizing:border-box;margin:0;padding:0}
  html,body{width:1200px;height:900px;overflow:hidden}
  body{background:var(--bg);font-family:"Arimo",Arial,sans-serif;color:var(--ink);position:relative}

  .sheet{position:absolute;background:var(--paper);box-shadow:0 6px 14px rgba(0,0,0,.25);overflow:hidden}

  /* brand name block */
  .brand{display:flex;align-items:center;gap:8px}
  .brand-name{font-weight:700;color:var(--brand-grey);letter-spacing:-.5px;line-height:1}
  .brand-dot{border-radius:50%;background:var(--orange);flex:none}

  /* footer band */
  .band{position:absolute;left:0;right:0;bottom:0;background:linear-gradient(90deg,var(--orange-deep),var(--orange))}
  .band::before{content:"";position:absolute;left:0;right:0;top:-7px;height:2px;background:var(--rule)}

  .contact{position:absolute;font-size:7px;line-height:1.45;color:var(--ink-soft)}
  .contact strong{color:var(--orange);font-weight:700}
  .contact b{color:var(--ink)}

  /* letterhead */
  .letterhead{left:60px;top:60px;width:420px;height:594px}
  .letterhead .brand{position:absolute;left:34px;top:34px}
  .letterhead .brand-name{font-size:30px}
  .letterhead .brand-dot{width:20px;height:20px}
  .letter-body{position:absolute;left:34px;top:110px;width:330px;font-size:7.2px;line-height:1.5;color:var(--ink-soft)}
  .letter-date{font-size:9px;color:var(--ink);margin-bottom:3px}
  .letter-subject{font-size:9px;font-weight:700;color:var(--orange);margin-bottom:12px}
  .letter-body p{margin-bottom:8px}
  .closing{position:absolute;left:34px;top:410px;font-size:7px;color:var(--ink-soft)}
  .signature{margin-top:8px;width:110px;height:40px;background:linear-gradient(90deg,#f4f4f4,#e6e6e6);border-radius:3px}
  .signer{margin-top:6px;font-weight:700;color:var(--ink);font-size:7.5px}
  .letterhead .contact{right:26px;bottom:42px;text-align:left;width:200px}
  .letterhead .band{height:20px}

  /* envelope front */
  .envelope-front{left:520px;top:60px;width:620px;height:290px}
  .envelope-front .brand{position:absolute;left:40px;top:44px}
  .envelope-front .brand-name{font-size:30px}
  .envelope-front .brand-dot{width:20px;height:20px}
  .address-window{position:absolute;left:40px;top:120px;width:250px;height:82px;border:1px solid #cfcfcf;border-radius:8px;background:linear-gradient(180deg,#fafafa,#e9e9e9)}
  .envelope-front .contact{right:30px;top:46px;width:220px}
  .envelope-front .band{height:18px}

  /* envelope back */
  .envelope-back{left:520px;top:375px;width:620px;height:290px}
  .envelope-back svg{position:absolute;left:0;top:0}

  /* business cards */
  .card{top:695px;width:255px;height:160px}
  .card-front .brand{position:absolute;left:20px;top:22px}
  .card-front .brand-name{font-size:22px}
  .card-front .brand-dot{width:14px;height:14px}
  .card-role{position:absolute;left:20px;top:62px;font-size:10px;font-weight:700;color:var(--orange)}
  .card-mail{position:absolute;left:20px;top:76px;font-size:7px;color:var(--ink-soft)}
  .card-front .contact{left:20px;bottom:22px;width:220px}
  .card-front .band{height:8px}
  .card-front .band::before{top:-5px;height:1px}
  .card-a{left:60px}
  .card-b{left:335px;background:linear-gradient(135deg,var(--orange-deep),var(--orange))}
  .card-c{left:610px}
  .card-d{left:885px;background:var(--paper-soft)}
  .card-mark{position:absolute;left:50%;top:50%;width:64px;height:64px;margin:-32px 0 0 -32px;border-radius:50%}
  .card-b .card-mark{background:var(--paper)}
  .card-d .card-mark{background:var(--orange)}
</style>
</head>
<body>

<!-- Letterhead -->
<section class="sheet letterhead">
  <div class="brand"><span class="brand-name">lumora</span><span class="brand-dot"></span></div>
  <div class="letter-body">
    <div class="letter-date">Date: 23 November 2013</div>
    <div class="letter-subject">RE: Lorem ipsum dolor sit amet</div>
    <p>Thank you for choosing our network services this year. We are glad to share the new look of our company and the way it will appear on every document you receive from us.</p>
    <p>Our team keeps improving speed, coverage and support across the region, and we will keep you informed about each upgrade as it arrives.</p>
    <p>Please contact our service desk with any questions about your plan, billing or installation.</p>
    <p>We look forward to working with you.</p>
  </div>
  <div class="closing">
    Yours sincerely,
    <div class="signature" role="img" aria-label="Handwritten signature"></div>
    <div class="signer">PAUL REYES</div>
    <div>Senior manager</div>
  </div>
  <div class="contact">
    <strong>Lumora - Telecomunicações e Internet</strong><br>
    Rua das Palmeiras, 410 - Centro Cep 13100-000 - Valinhos - SP<br>
    Tel: (11) 4000-2710 web: <b>www.lumora.com.br</b>
  </div>
  <div class="band"></div>
</section>

<!-- Envelope front -->
<section class="sheet envelope-front">
  <div class="brand"><span class="brand-name">lumora</span><span class="brand-dot"></span></div>
  <div class="address-window"></div>
  <div class="contact">
    <strong>Lumora - Telecomunicações e Internet</strong><br>
    Rua das Palmeiras, 410 - Centro Cep 13100-000 - Valinhos - SP<br>
    Tel: (11) 4000-2710 web: <b>www.lumora.com.br</b>
  </div>
  <div class="band"></div>
</section>

<!-- Envelope back -->
<section class="sheet envelope-back">
  <svg width="620" height="290" viewBox="0 0 620 290" aria-hidden="true">
    <defs>
      <linearGradient id="flapFill" x1="0" y1="0" x2="1" y2="0">
        <stop offset="0" stop-color="#c9500a"/>
        <stop offset="1" stop-color="#ee6a10"/>
      </linearGradient>
    </defs>
    <path d="M0 0 H620 V18 Q600 40 560 48 L40 118 Q10 122 0 112 Z" fill="url(#flapFill)"/>
    <circle cx="310" cy="190" r="52" fill="#ececec"/>
  </svg>
</section>

<!-- Business card fronts and backs -->
<section class="sheet card card-front card-a">
  <div class="brand"><span class="brand-name">lumora</span><span class="brand-dot"></span></div>
  <div class="card-role">Atendimento</div>
  <div class="card-mail">atendimento@lumora.com.br</div>
  <div class="contact">
    <strong>Lumora - Telecomunicações e Internet</strong><br>
    Rua das Palmeiras, 410 - Centro Cep 13100-000<br>
    Tel: (11) 4000-2710 &nbsp; <b>www.lumora.com.br</b>
  </div>
  <div class="band"></div>
</section>

<section class="sheet card card-b"><span class="card-mark"></span></section>

<section class="sheet card card-front card-c">
  <div class="brand"><span class="brand-name">lumora</span><span class="brand-dot"></span></div>
  <div class="card-role">Atendimento</div>
  <div class="card-mail">atendimento@lumora.com.br</div>
  <div class="contact">
    <strong>Lumora - Telecomunicações e Internet</strong><br>
    Rua das Palmeiras, 410 - Centro Cep 13100-000<br>
    Tel: (11) 4000-2710 &nbsp; <b>www.lumora.com.br</b>
  </div>
  <div class="band"></div>
</section>

<section class="sheet card card-d"><span class="card-mark"></span></section>

</body>
</html>
```